Cannabis Processor Vape Cart Box Design/Concentrate Jar Box Design

We are a solventless (no chemicals added) cannabis processor in the state of Michigan. We have 2 products, one is a vape cartridge and one is a 5mL clear glass concentrate jar with a black lid. We need designs that correlates with our logo for their box packaging. Each piece of packaging has an opening so you can see the jar/vape cartridge and their contents. Each piece of packaging needs to have the universal symbol of cannabis, which is on the bottom right hand corner of the vape cartridge container for reference. Also on the jar box top lid we need the net weight listed like this (NET WT. 1.0g / 0.0176oz) I have attached some examples of the packaging boxes, the jar we will be using, and our logo so you know what you are shooting for. On the Jar Box there will be a hole in the center of the bottom of the box, so people can see the jar and it's contents. On the back of the jar box I would like the following (Here at 842 Resins, our mission is to be make the purest concentrates available. We strive to fully represent the true essence of the flower through our solventless processes. At 842 Resins we only use the finest Michigan grown, pesticide-free flowers for extraction. We pride ourselves on our chemical-free extraction methods, and are constantly innovating to bring better and cleaner concentrates for Medicinal and Recreational use.) On the Vape Cartridge box there will be a straight up and down hole in the shape of the vape cartridge instead of the Michigan shape. Get creative, but remember that you can not use any cannabis leaf symbol on the design. On the top of the back of the vape cartridge box I want the following (Here at 842 Resins, our mission is to be make the purest vape cartridge available. We strive to fully represent the true essence of the flower through our solventless processes. At 842 Resins we only use the finest Michigan grown, pesticide-free flowers for extraction. We pride ourselves on our chemical-free extraction methods, and are constantly innovating to bring better and cleaner products for both Medicinal and Recreational use.) We look forward to your submissions, and to the best design we thank you in advance. I almost forgot, we would prefer a black base with white lettering, but we are open to any creative ideas, so please submit more options than what we requested, because the best look will win.

```html
<!DOCTYPE html>
<html lang="en">
<head>
<meta charset="utf-8">
<title>842 Resins — Packaging Panels</title>
<link rel="stylesheet" href="https://fonts.googleapis.com/css2?family=Cinzel:wght@400;500&display=swap">
<style>
  :root{
    --stage:#d9d9d9;
    --box-black:#141414;
    --box-charcoal:#262626;
    --spine:#1a1a1a;
    --ink-white:#f4f4f4;
    --gold:#e8c440;
    --band-yellow:#e6cc55;
    --band-ink:#2a2a2a;
    --badge-green:#3f7a45;
    --badge-dark:#1d3b22;
    --window:#efefef;
    --rule:#3a3a3a;
  }
  *{margin:0;padding:0;box-sizing:border-box}
  html,body{width:1200px;height:709px;overflow:hidden;background:var(--stage)}
  body{position:relative;font-family:"Cinzel",serif;color:var(--ink-white)}

  .brand-name{font-weight:400;color:var(--ink-white);letter-spacing:.06em;white-space:nowrap}

  /* ---------- Vape cartridge box ---------- */
  .cart-box{position:absolute;left:60px;top:34px;width:336px;height:636px}
  .cart-spine{position:absolute;left:0;top:76px;width:52px;height:560px;
    background:linear-gradient(180deg,#222 0%,var(--spine) 60%,#0e0e0e 100%);
    border-right:1px solid #0a0a0a}
  .cart-spine .brand-name{position:absolute;left:50%;top:50%;
    transform:translate(-50%,-50%) rotate(-90deg);font-size:20px;letter-spacing:.12em}
  .cart-hang-tab{position:absolute;left:52px;top:0;width:284px;height:76px;
    background:var(--box-charcoal);border-radius:2px 2px 0 0}
  .cart-hang-tab svg{position:absolute;left:0;top:0}
  .cart-front{position:absolute;left:52px;top:76px;width:284px;height:560px;overflow:hidden;
    background:linear-gradient(160deg,#2e2e2e 0%,#1c1c1c 55%,#111 100%)}
  .cart-flask-art{position:absolute;left:42px;top:150px;width:200px;height:300px;
    background:radial-gradient(ellipse at 50% 65%,rgba(0,0,0,.35),rgba(0,0,0,0) 70%)}
  .cart-front .brand-name{position:absolute;top:62px;left:0;right:0;text-align:center;font-size:28px}
  .cart-product{position:absolute;top:118px;left:0;right:0;text-align:center;
    font-size:14px;letter-spacing:.08em;color:var(--gold)}
  .cart-window{position:absolute;left:107px;top:170px;width:70px;height:220px;
    border-radius:35px;background:var(--window)}
  .cart-bands{position:absolute;left:10px;right:10px;bottom:50px;height:72px}
  .cart-band{position:absolute;top:10px;height:54px;width:90px;background:var(--band-yellow);
    color:var(--band-ink);font-size:10.5px;line-height:1.2;text-align:center;
    display:flex;align-items:center;justify-content:center;letter-spacing:.01em}
  .cart-band--left{left:0}
  .cart-band--right{right:0}
  .cart-badge{position:absolute;left:50%;top:0;transform:translateX(-50%)}

  /* ---------- Jar box ---------- */
  .jar-top{position:absolute;left:470px;top:34px;width:390px;height:390px;background:var(--box-black)}
  .jar-top-frame{position:absolute;inset:16px;border:3px solid var(--rule)}
  .jar-top .brand-name{position:absolute;top:48px;right:44px;font-size:22px}
  .jar-window{position:absolute;left:125px;top:125px;width:140px;height:140px;border-radius:50%;
    border:4px solid var(--gold);background:var(--box-black);padding:5px}
  .jar-window span{display:block;width:100%;height:100%;border-radius:50%;background:var(--window)}
  .jar-top .jar-badge{position:absolute;right:50px;bottom:40px}

  .jar-front{position:absolute;left:470px;top:436px;width:390px;height:230px;background:var(--box-black)}
  .jar-front .brand-name{position:absolute;top:62px;left:0;right:0;text-align:center;font-size:30px}
  .net-weight{position:absolute;bottom:44px;left:0;right:0;text-align:center;font-size:11px;
    letter-spacing:.05em;color:var(--ink-white)}

  .jar-side{position:absolute;left:872px;top:436px;width:290px;height:230px;background:#111}
  .jar-mission{position:absolute;left:26px;right:26px;top:86px;text-align:center;
    font-size:10px;line-height:1.6;letter-spacing:.03em;color:var(--ink-white)}
</style>
</head>
<body>

<section class="cart-box" aria-label="Vape cartridge box">
  <div class="cart-hang-tab">
    <svg width="284" height="76" viewBox="0 0 284 76" aria-hidden="true">
      <path d="M107 40 h22 a8 8 0 0 1 8 -8 h10 a8 8 0 0 1 8 8 h22 a10 10 0 0 1 0 20 h-70 a10 10 0 0 1 0 -20z" fill="var(--stage)"/>
    </svg>
  </div>
  <div class="cart-spine" aria-label="Vape cartridge box side">
    <div class="brand-name">842 Resins</div>
  </div>
  <div class="cart-front">
    <div class="cart-flask-art" role="img" aria-label="Faint lab flask background artwork"></div>
    <div class="brand-name">842 Resins</div>
    <div class="cart-product">VAPE CARTRIDGE</div>
    <div class="cart-window" aria-label="Cartridge viewing window"></div>
    <div class="cart-bands">
      <div class="cart-band cart-band--left">MICHIGAN<br>GROWN AND<br>EXTRACTED</div>
      <svg class="cart-badge" width="76" height="70" viewBox="0 0 76 70" aria-label="Universal cannabis symbol">
        <path d="M3 3 H73 L38 67 Z" fill="var(--badge-dark)" stroke="var(--badge-green)" stroke-width="5" stroke-linejoin="round"/>
      </svg>
      <div class="cart-band cart-band--right">PREMIUM<br>CANNABIS<br>DISTILLATE</div>
    </div>
  </div>
</section>

<section class="jar-top" aria-label="Jar box top">
  <div class="jar-top-frame"></div>
  <div class="brand-name">842 Resins</div>
  <div class="jar-window" aria-label="Jar viewing window"><span></span></div>
  <svg class="jar-badge" width="52" height="46" viewBox="0 0 52 46" aria-label="Universal cannabis symbol">
    <path d="M3 3 H49 L26 43 Z" fill="var(--badge-dark)" stroke="var(--badge-green)" stroke-width="4" stroke-linejoin="round"/>
  </svg>
</section>

<section class="jar-front" aria-label="Jar box front">
  <div class="brand-name">842 Resins</div>
  <div class="net-weight">NET WT. 1.0G / 0.0176OZ</div>
</section>

<section class="jar-side" aria-label="Jar box side">
  <p class="jar-mission">At 842 Resins we only use the finest Michigan grown, pesticide-free flowers for extraction</p>
</section>

</body>
</html>
```